#1 Selling Sweden weight loss supplement comes to USA - LABEL needed!

The number one weight loss in Sweden is coming to USA

-I need a label that is clean and simple but somehow represents, in an abstract way, weight loss or slender.
-The product and water mixed is all the is needed. This too could be represented in the label design.
-The bottle will be white.

-Attached is a picture of a supplement bottle with
--the logo for the company, 'NuKelvara'
--the name of the supplement, 'Kelvara Lithe'
and
--other text that could be included in the final label.

ALSO attached are 2 label designs that I like. This might give you an idea of a direction to go.
Thank You very much.

Target Market(s)

Health conscience people

Industry/Entity Type

Weight

Font styles to use
Sans Serif

Requirements
Must have
• -Size of bottle - 2" wide x 4" high
Nice to have
• *Lowers Hunger up to 50%
• *Decreases cravings or unhealthy foods up to 90%
• *Enhances Weight Loss
• " A Durovix a day keeps hunger away"

```html
<!DOCTYPE html>
<html lang="en">
<head>
<meta charset="utf-8">
<title>Kelvara Lithe Label</title>
<link rel="stylesheet" href="https://fonts.googleapis.com/css2?family=Questrial&display=swap">
<style>
  :root {
    --page-bg: #ffffff;
    --label-top: #c9cbcd;
    --label-mid: #eef0f1;
    --label-bottom: #ffffff;
    --ink: #1c1c1c;
    --ink-soft: #2b2b2b;
    --band: #222222;
    --band-text: #d6d6d6;
  }
  * { box-sizing: border-box; margin: 0; padding: 0; }
  html, body {
    width: 1200px;
    height: 1000px;
    overflow: hidden;
    background: var(--page-bg);
    font-family: "Questrial", "Helvetica Neue", Arial, sans-serif;
  }
  .canvas {
    position: relative;
    width: 1200px;
    height: 1000px;
    display: flex;
    align-items: center;
    justify-content: center;
  }
  .label {
    position: relative;
    width: 760px;
    height: 900px;
    border-radius: 44px;
    overflow: hidden;
    background: linear-gradient(180deg, var(--label-top) 0%, var(--label-mid) 38%, var(--label-bottom) 100%);
    display: flex;
    flex-direction: column;
    align-items: center;
    color: var(--ink);
    text-align: center;
  }
  .brand {
    margin-top: 60px;
    display: flex;
    align-items: center;
    gap: 14px;
    font-size: 52px;
    color: var(--ink-soft);
    letter-spacing: 0.5px;
  }
  .brand-dot {
    width: 22px;
    height: 22px;
    border-radius: 50%;
    background: var(--ink-soft);
  }
  .product-name {
    margin-top: 70px;
    font-size: 112px;
    line-height: 1.05;
    font-weight: 400;
    letter-spacing: 1px;
  }
  .product-type {
    margin-top: 46px;
    font-size: 44px;
    line-height: 1.2;
  }
  .ingredient {
    font-size: 44px;
    line-height: 1.3;
  }
  .ingredient sup { font-size: 20px; }
  .claims {
    margin-top: 40px;
    list-style: none;
    font-size: 19px;
    line-height: 2;
    text-transform: uppercase;
  }
  .tagline {
    margin-top: 8px;
    font-size: 14px;
    font-style: italic;
    text-transform: uppercase;
    letter-spacing: 0.3px;
  }
  .net-weight {
    position: absolute;
    left: 0;
    right: 0;
    bottom: 0;
    height: 92px;
    background: var(--band);
    color: var(--band-text);
    font-size: 34px;
    display: flex;
    align-items: center;
    justify-content: center;
    letter-spacing: 0.5px;
  }
</style>
</head>
<body>
  <main class="canvas">
    <section class="label">
      <div class="brand">
        <span class="brand-name">NuKelvara</span>
        <span class="brand-dot"></span>
      </div>
      <h1 class="product-name">KELVARA<br>LITHE</h1>
      <p class="product-type">Protein Powder</p>
      <p class="ingredient">Durovix<sup>®</sup></p>
      <ul class="claims">
        <li>Lowers hunger up to 50%</li>
        <li>Decreases cravings or unhealthy foods up to 90%</li>
        <li>Enhances weight loss</li>
      </ul>
      <p class="tagline">A Durovix a day keeps hunger away</p>
      <div class="net-weight">NET WT 250 G (8.84 oz)</div>
    </section>
  </main>
</body>
</html>
```